Unique and original Business Card for Financial Services Business

I have moved premises and need to change the detail on my business card so thought now is a good time for a re-design. Looking for something professional and modern with colours to fit in with out logo. Like the idea of foil or embossing if that works but not a must have but I do want something that stands out and that I could not design myself.

Once business card is designed I will also be looking to get letterhead and flyers done but want the business card concept in place first.

The majority of designs I am receiving are generic and template based. I am looking for something unique and original. We have some great design elements in our logo, think outside the box and show me something that stands out from the crowd.

Target Market(s)

Business Professionals

Industry/Entity Type

Finance

Contact Information for Business Card

Name: Delia Norwood Phone 0473 958 162 Address PO Box 8617 Mossvale NSW 2389 Email info@steadyharbourfinancialservices.com.au website www.steadyharbourfinancialservices.com.au

Font styles to use
Other font styles liked:
• Ralway

Requirements
Should not have
• No black backgrounds please

```html
<!DOCTYPE html>
<html lang="en">
<head>
<meta charset="utf-8">
<title>Steady Harbour Financial Services – Business Card</title>
<link rel="stylesheet" href="https://fonts.googleapis.com/css2?family=Roboto+Condensed:wght@300;700&display=swap">
<style>
  :root {
    --backdrop: #e6e7e8;
    --teal: #00a29b;
    --teal-deep: #0f7f86;
    --navy: #08243a;
    --white: #ffffff;
    --card-shadow: 0 4px 14px rgba(0, 0, 0, 0.22);
  }
  * { margin: 0; padding: 0; box-sizing: border-box; }
  html, body {
    width: 1200px;
    height: 1200px;
    overflow: hidden;
    background: var(--backdrop);
    font-family: "Roboto Condensed", "Arial Narrow", sans-serif;
  }
  .canvas {
    position: relative;
    width: 1200px;
    height: 1200px;
  }
  .card {
    position: absolute;
    left: 150px;
    width: 900px;
    height: 525px;
    box-shadow: var(--card-shadow);
    overflow: hidden;
  }

  /* ---------- Front ---------- */
  .card-front {
    top: 56px;
    background: linear-gradient(90deg, var(--teal) 0%, #038d90 35%, #065a6e 70%, var(--navy) 100%);
    color: var(--white);
  }
  .front-illustration {
    position: absolute;
    left: 80px;
    top: 0;
    width: 400px;
    height: 440px;
    background: radial-gradient(ellipse 50% 50% at 48% 48%, rgba(255,255,255,0.55) 0%, rgba(255,255,255,0.3) 55%, rgba(255,255,255,0) 100%);
  }
  .identity {
    position: absolute;
    right: 100px;
    top: 108px;
    text-align: right;
  }
  .identity-name {
    font-weight: 700;
    font-size: 47px;
    line-height: 1;
    letter-spacing: 0.2px;
  }
  .identity-role {
    margin-top: 14px;
    font-weight: 300;
    font-size: 19px;
  }
  .contact-list {
    position: absolute;
    right: 92px;
    top: 264px;
    list-style: none;
    text-align: right;
    font-weight: 300;
    font-size: 19px;
  }
  .contact-item {
    display: flex;
    justify-content: flex-end;
    align-items: center;
    height: 35px;
  }
  .contact-item.address { margin-top: 27px; }
  .contact-icon {
    width: 14px;
    height: 14px;
    margin-left: 16px;
    flex: none;
  }

  /* ---------- Back ---------- */
  .card-back {
    top: 616px;
    background: var(--white);
  }
  .back-arcs {
    position: absolute;
    left: 0;
    top: 0;
  }
  .brand {
    position: absolute;
    left: 0;
    right: 0;
    top: 125px;
    text-align: center;
    color: var(--teal-deep);
    font-weight: 300;
  }
  .brand-dot {
    display: block;
    width: 150px;
    height: 150px;
    margin: 0 auto 28px;
    border-radius: 50%;
    background: var(--teal-deep);
  }
  .brand-name {
    display: block;
    font-size: 72px;
    line-height: 1;
    letter-spacing: 0;
    text-transform: uppercase;
  }
  .brand-tagline {
    display: block;
    margin-top: 4px;
    font-size: 34px;
    letter-spacing: 17px;
    padding-left: 17px;
  }
</style>
</head>
<body>
<main class="canvas">

  <section class="card card-front" aria-label="Business card front">
    <div class="front-illustration" role="img" aria-label="White hummingbird silhouette in flight with sweeping feather curves"></div>

    <div class="identity">
      <h1 class="identity-name">Delia Norwood</h1>
      <p class="identity-role">Director</p>
    </div>

    <ul class="contact-list">
      <li class="contact-item">0473 958 162
        <svg class="contact-icon" viewBox="0 0 16 16" aria-hidden="true"><path d="M4 1.5 L6.3 4.8 L4.9 6.4 C5.7 8.2 7.8 10.3 9.6 11.1 L11.2 9.7 L14.5 12 L13 14.5 C7.5 14.5 1.5 8.5 1.5 3 Z" fill="var(--white)"/></svg>
      </li>
      <li class="contact-item">info@steadyharbourfinancialservices.com.au
        <svg class="contact-icon" viewBox="0 0 16 16" aria-hidden="true"><rect x="1" y="3" width="14" height="10" fill="var(--white)"/><path d="M1.5 3.5 L8 9 L14.5 3.5" fill="none" stroke="#0a4a5e" stroke-width="1.3"/></svg>
      </li>
      <li class="contact-item">www.steadyharbourfinancialservices.com.au
        <svg class="contact-icon" viewBox="0 0 16 16" aria-hidden="true"><circle cx="8" cy="8" r="6.5" fill="none" stroke="var(--white)" stroke-width="1.5"/><ellipse cx="8" cy="8" rx="2.8" ry="6.5" fill="none" stroke="var(--white)" stroke-width="1.2"/><path d="M1.5 8 H14.5" stroke="var(--white)" stroke-width="1.2"/></svg>
      </li>
      <li class="contact-item address">PO Box 8617 Mossvale NSW 2389
        <svg class="contact-icon" viewBox="0 0 16 16" aria-hidden="true"><path d="M8 1 C5.2 1 3.5 3 3.5 5.4 C3.5 8.5 8 12 8 12 C8 12 12.5 8.5 12.5 5.4 C12.5 3 10.8 1 8 1 Z" fill="none" stroke="var(--white)" stroke-width="1.5"/><circle cx="8" cy="5.4" r="1.6" fill="var(--white)"/><path d="M2.5 14.5 H13.5" stroke="var(--white)" stroke-width="1.5"/></svg>
      </li>
    </ul>
  </section>

  <section class="card card-back" aria-label="Business card back">
    <svg class="back-arcs" width="900" height="525" viewBox="0 0 900 525" aria-hidden="true">
      <defs>
        <linearGradient id="arc-fade-top" x1="1" y1="0" x2="0" y2="1">
          <stop offset="0" stop-color="var(--teal)" stop-opacity="0"/>
          <stop offset="0.5" stop-color="var(--teal-deep)"/>
          <stop offset="1" stop-color="var(--navy)"/>
        </linearGradient>
        <linearGradient id="arc-fade-bottom" x1="0" y1="1" x2="1" y2="0">
          <stop offset="0" stop-color="var(--teal)" stop-opacity="0"/>
          <stop offset="0.5" stop-color="var(--teal-deep)"/>
          <stop offset="1" stop-color="var(--teal)"/>
        </linearGradient>
      </defs>
      <path d="M225 75 C150 80 95 140 88 209" fill="none" stroke="url(#arc-fade-top)" stroke-width="3"/>
      <path d="M669 450 C740 448 805 390 810 315" fill="none" stroke="url(#arc-fade-bottom)" stroke-width="3"/>
    </svg>

    <div class="brand">
      <span class="brand-dot" aria-hidden="true"></span>
      <span class="brand-name">Steady Harbour</span>
      <span class="brand-tagline">Financial Services</span>
    </div>
  </section>

</main>
</body>
</html>
```